Fernvale Business Card Design

We are looking for a fresh business card design for our new logo. We would like a business card that is unique but friendly. We are in the window coverings business offering blinds, shutters and shades for homes.

Target Market(s)

Targeting the end-consumer

Industry/Entity Type

Business

Requirements
Must have
• Must have a dedicates space for a photo of our sales person. Must contain our new logo (attached).

```html
<!DOCTYPE html>
<html lang="en">
<head>
<meta charset="utf-8">
<title>Fernvale Business Card</title>
<link href="https://fonts.googleapis.com/css2?family=Roboto:wght@400;500;700&display=swap" rel="stylesheet">
<style>
  :root {
    --stage: #1b1b1d;
    --card-grey: #5f6064;
    --card-white: #ffffff;
    --ink-grey: #5c5d61;
    --leaf-green: #7cc242;
    --text-light: #ffffff;
    --text-soft: #e4e4e6;
    --photo-dark: #2a2426;
    --photo-light: #8a8688;
  }
  * { margin: 0; padding: 0; box-sizing: border-box; }
  html, body { width: 1200px; height: 900px; overflow: hidden; }
  body {
    background: var(--stage);
    font-family: "Roboto", Arial, sans-serif;
    position: relative;
  }
  .card {
    position: absolute;
    width: 540px;
    height: 310px;
    border-radius: 4px;
    box-shadow: 0 18px 40px rgba(0,0,0,.55);
    overflow: hidden;
  }

  /* Front: grey card with salesperson */
  .card-front {
    left: 60px;
    top: 520px;
    top: 500px;
    background: var(--card-grey);
    color: var(--text-light);
  }
  .card-front .photo {
    position: absolute;
    left: 110px;
    top: 0;
    width: 170px;
    height: 130px;
    background: linear-gradient(160deg, var(--photo-light) 0%, var(--photo-dark) 70%);
  }
  .card-front .person {
    position: absolute;
    left: 40px;
    top: 100px;
  }
  .person-name {
    font-size: 19px;
    font-weight: 700;
    letter-spacing: .5px;
  }
  .person-role {
    font-size: 12.5px;
    color: var(--text-soft);
    margin-top: 2px;
  }
  .card-front .divider {
    position: absolute;
    left: 40px;
    right: 40px;
    top: 150px;
    height: 2px;
    background: var(--text-light);
  }
  .card-front .brand {
    position: absolute;
    right: 40px;
    top: 52px;
    display: flex;
    align-items: center;
    gap: 10px;
  }
  .brand-square {
    width: 30px;
    height: 30px;
    border: 2px solid var(--text-light);
  }
  .brand-name {
    font-size: 40px;
    font-weight: 500;
  }
  .card-front .address {
    position: absolute;
    left: 40px;
    top: 172px;
    width: 220px;
    font-size: 13px;
    line-height: 1.5;
    color: var(--text-soft);
  }
  .card-front .contacts {
    position: absolute;
    right: 40px;
    top: 170px;
    list-style: none;
    font-size: 14px;
    line-height: 1.75;
  }
  .contacts li { display: flex; align-items: center; gap: 8px; }
  .contacts svg { width: 13px; height: 13px; fill: var(--text-light); flex: none; }

  /* Back: white card with name */
  .card-back {
    left: 600px;
    top: 90px;
    background: var(--card-white);
  }
  .card-back .brand {
    position: absolute;
    right: 44px;
    bottom: 58px;
    display: flex;
    align-items: center;
    gap: 12px;
  }
  .card-back .brand-square {
    width: 34px;
    height: 34px;
    border: none;
    background: var(--leaf-green);
  }
  .card-back .brand-name {
    font-size: 52px;
    color: var(--ink-grey);
  }
  .card-back .web {
    position: absolute;
    right: 46px;
    bottom: 32px;
    font-size: 15px;
    color: var(--leaf-green);
    font-weight: 500;
  }
</style>
</head>
<body>

<section class="card card-back">
  <div class="brand">
    <span class="brand-square"></span>
    <span class="brand-name">Fernvale</span>
  </div>
  <p class="web">www.fernvale.com</p>
</section>

<section class="card card-front">
  <div class="photo" role="img" aria-label="Photo of the salesperson"></div>
  <div class="person">
    <p class="person-name">DANIEL PRICE</p>
    <p class="person-role">Managing Director</p>
  </div>
  <div class="brand">
    <span class="brand-square"></span>
    <span class="brand-name">Fernvale</span>
  </div>
  <div class="divider"></div>
  <p class="address">42 Meadow Park Drive, Suite 210, Lakeside, NJ</p>
  <ul class="contacts">
    <li>
      <svg viewBox="0 0 16 16" aria-hidden="true"><path d="M3 1h3l1.5 4-2 1.3a9 9 0 0 0 4.2 4.2L11 8.5l4 1.5v3a2 2 0 0 1-2 2A12 12 0 0 1 1 3a2 2 0 0 1 2-2z"/></svg>
      27 10 004 1187
    </li>
    <li>
      <svg viewBox="0 0 16 16" aria-hidden="true"><path d="M1 3h14v10H1z M2 4l6 5 6-5" fill="none" stroke="#fff" stroke-width="1.6"/></svg>
      daniel@fernvale.com
    </li>
    <li>
      <svg viewBox="0 0 16 16" aria-hidden="true"><circle cx="8" cy="8" r="6.5" fill="none" stroke="#fff" stroke-width="1.4"/><path d="M1.5 8h13M8 1.5c-3 3.5-3 9.5 0 13M8 1.5c3 3.5 3 9.5 0 13" fill="none" stroke="#fff" stroke-width="1.2"/></svg>
      www.fernvale.com
    </li>
  </ul>
</section>

</body>
</html>
```